Welding and farication business card

Business name Tbm Welding & Fabrication

I need a business card made for my welding and fabrication business that is bold and stands out. My business is both welding repairs on machinery and anything else you can imagine as well as fabricating new products. i have used this service before and was very happy with the out come of my design logo. i think the card should remain fairly simple and classy but also be bold. I think a black card would best be suited to the talk with my logo on it. i feel the back of the card should just have my logo and the front have my logo email, website and phone number and maybe incorporate a facebook and instagram simple if it can be made look good these arnt a necessity.
I have included both my logo and some business card ideas below

Target Market(s)

Farmers, heavy industry, earthmoving, trucking

Industry/Entity Type

Engineering

Contact Information for Business Card

0438517264
dale@tbmweldingandfabrication.com.au
www.tbmweldingandfabrication.com.au

Colors
33a6d7
0255a3

Requirements
Must have
• Dale Hutchins
my phone number 0438517264
my logo
Preferably a black card desgn
Nice to have
• List of what i do,
Sheds and carports
Ute trays
Stockyards
Trailers
Farm equipment
Stockcrates
Gateways and Entrances
Breakdowns
Maintenance
And lots more!

```html
<!DOCTYPE html>
<html lang="en">
<head>
<meta charset="utf-8">
<title>Tbm Welding &amp; Fabrication – Business Card</title>
<link rel="stylesheet" href="https://fonts.googleapis.com/css2?family=Roboto:ital,wght@0,400;0,700;0,900;1,400;1,700&display=swap">
<style>
  :root {
    --stage: #2b2b2d;
    --card: #1c1c1e;
    --ink: #ffffff;
    --ink-soft: #e6e6e6;
    --sky: #33a6d7;
    --navy: #0255a3;
  }
  * { margin: 0; padding: 0; box-sizing: border-box; }
  html, body {
    width: 1200px; height: 900px; overflow: hidden;
    background: var(--stage);
    font-family: "Roboto", Arial, sans-serif;
  }
  .stage {
    width: 1200px; height: 900px;
    display: flex; flex-direction: column;
    align-items: center; justify-content: center; gap: 40px;
  }
  .card {
    width: 700px; height: 400px;
    background: var(--card);
    border-radius: 4px;
    box-shadow: 0 14px 30px rgba(0,0,0,.45);
    position: relative;
  }

  /* Back: brand + services */
  .card-back {
    display: flex; flex-direction: column;
    align-items: center; justify-content: center;
  }
  .brand {
    display: flex; align-items: center; gap: 16px;
  }
  .brand-dot {
    width: 22px; height: 22px; border-radius: 50%;
    background: var(--sky);
  }
  .brand-name {
    color: var(--ink);
    font-weight: 900;
    font-size: 38px;
    letter-spacing: .5px;
    text-transform: uppercase;
  }
  .services {
    margin-top: 42px;
    text-align: center;
    color: var(--ink-soft);
    font-size: 17px;
    line-height: 1.6;
  }
  .services .sep { color: var(--sky); margin: 0 7px; }

  /* Front: person + contacts */
  .card-front {
    display: flex; align-items: center; justify-content: center;
    gap: 30px;
  }
  .person { text-align: right; }
  .person-name {
    color: var(--sky);
    font-weight: 700; font-style: italic;
    font-size: 30px; text-transform: uppercase;
  }
  .person-role {
    color: var(--ink-soft);
    font-style: italic; font-size: 19px; margin-top: 4px;
  }
  .divider {
    width: 2px; height: 110px; background: var(--sky);
    transform: skewX(-20deg);
  }
  .contacts { list-style: none; }
  .contacts li {
    display: flex; align-items: center; gap: 10px;
    color: var(--ink-soft); font-size: 17px; line-height: 1.75;
  }
  .contacts svg { width: 16px; height: 16px; fill: var(--sky); flex: none; }
</style>
</head>
<body>
<main class="stage">

  <section class="card card-back" aria-label="Card back">
    <div class="brand">
      <span class="brand-dot"></span>
      <span class="brand-name">Tbm Welding &amp; Fabrication</span>
    </div>
    <p class="services">
      Sheds<span class="sep">•</span>Ute trays<span class="sep">•</span>Cattle and sheep yards<span class="sep">•</span>Trailers<br>
      Farm equipment<span class="sep">•</span>Gateways and Entrances<span class="sep">•</span>And lots more!
    </p>
  </section>

  <section class="card card-front" aria-label="Card front">
    <div class="person">
      <h1 class="person-name">Dale Hutchins</h1>
      <p class="person-role">President</p>
    </div>
    <span class="divider"></span>
    <ul class="contacts">
      <li>
        <svg viewBox="0 0 24 24" aria-hidden="true"><path d="M6.6 10.8a15 15 0 0 0 6.6 6.6l2.2-2.2a1 1 0 0 1 1-.25 11.4 11.4 0 0 0 3.6.57 1 1 0 0 1 1 1V20a1 1 0 0 1-1 1A17 17 0 0 1 3 4a1 1 0 0 1 1-1h3.5a1 1 0 0 1 1 1c0 1.25.2 2.45.57 3.57a1 1 0 0 1-.25 1z"/></svg>
        0438517264
      </li>
      <li>
        <svg viewBox="0 0 24 24" aria-hidden="true"><path d="M2 5h20v14H2z M2 5l10 8 10-8" fill="none" stroke="#33a6d7" stroke-width="2"/></svg>
        dale@tbmweldingandfabrication.com.au
      </li>
      <li>
        <svg viewBox="0 0 24 24" aria-hidden="true"><circle cx="12" cy="12" r="9" fill="none" stroke="#33a6d7" stroke-width="2"/><path d="M3 12h18M12 3c3 3 3 15 0 18M12 3c-3 3-3 15 0 18" fill="none" stroke="#33a6d7" stroke-width="1.6"/></svg>
        www.tbmweldingandfabrication.com.au
      </li>
    </ul>
  </section>

</main>
</body>
</html>
```